Album art for soul / electronic band

Album art for a singer / producer duo. Art should be similar to the copper lantern album art and be consistent with the color scheme in the attached band photo. The name of the album is corvelha (portuguese for delicate). Please do not include the photo in your design. Design should center around water.

Target Market(s)

Gen X / Millenial soul music fans

Industry/Entity Type

music

Font styles to use
Sans Serif

Requirements
Must have
• Clean modern look, photo or artwork.
Nice to have
• It should look like album art from groups in the same genre such as the Copper Lantern, Brasskite, K. Dunmore, Orrin Vale
Should not have
• band photo, musical notes, any music iconography

```html
<!DOCTYPE html>
<html lang="en">
<head>
<meta charset="utf-8">
<title>Corvelha — Album Cover</title>
<link rel="stylesheet" href="https://fonts.googleapis.com/css2?family=Montserrat:wght@300;400;500&display=swap">
<style>
  :root {
    --backdrop: #b5c2bf;
    --cover-top: #1a2121;
    --cover-mid: #353d3d;
    --cover-low: #6f7877;
    --cover-mist: #a3aba8;
    --figure-tone: #4e5756;
    --ripple-line: rgba(222, 232, 229, 0.32);
    --title-ink: #e9efed;
    --title-glow: rgba(150, 200, 195, 0.6);
    --caption-ink: #dfe5e3;
    --artist-ink: #2b3232;
  }
  * { margin: 0; padding: 0; box-sizing: border-box; }
  html, body {
    width: 1200px;
    height: 807px;
    overflow: hidden;
    background: var(--backdrop);
    font-family: "Montserrat", sans-serif;
  }
  .stage {
    position: relative;
    width: 1200px;
    height: 807px;
  }
  .album-cover {
    position: absolute;
    left: 240px;
    top: 43px;
    width: 720px;
    height: 720px;
    overflow: hidden;
    background: linear-gradient(180deg, var(--cover-top) 0%, var(--cover-mid) 42%, var(--cover-low) 78%, var(--cover-mist) 100%);
    box-shadow: 0 12px 30px rgba(0, 0, 0, 0.25);
  }
  .cover-artwork {
    position: absolute;
    left: 130px;
    top: 170px;
    width: 460px;
    height: 430px;
    background:
      linear-gradient(180deg, rgba(78, 87, 86, 0) 0%, rgba(78, 87, 86, 0.85) 30%, rgba(90, 99, 98, 0.7) 70%, rgba(150, 158, 155, 0) 100%);
    -webkit-mask: radial-gradient(ellipse 48% 50% at 50% 50%, #000 55%, transparent 100%);
            mask: radial-gradient(ellipse 48% 50% at 50% 50%, #000 55%, transparent 100%);
  }
  .water-surface {
    position: absolute;
    left: 0;
    bottom: 0;
    width: 720px;
    height: 220px;
  }
  .mist-band {
    position: absolute;
    left: 0;
    bottom: 70px;
    width: 100%;
    height: 160px;
    background: radial-gradient(ellipse 55% 50% at 50% 60%, rgba(205, 212, 209, 0.45) 0%, rgba(205, 212, 209, 0) 100%);
  }
  .album-title {
    position: absolute;
    top: 34px;
    left: 0;
    width: 100%;
    text-align: center;
    font-weight: 500;
    font-size: 62px;
    line-height: 1;
    letter-spacing: 9px;
    padding-left: 9px;
    color: var(--title-ink);
    text-shadow: -3px 2px 0 var(--title-glow);
  }
  .album-subtitle {
    position: absolute;
    top: 106px;
    left: 0;
    width: 100%;
    text-align: center;
    font-weight: 400;
    font-size: 25px;
    line-height: 1;
    letter-spacing: 0.5px;
    color: var(--caption-ink);
  }
  .artist-name {
    position: absolute;
    top: 664px;
    left: 0;
    width: 100%;
    text-align: center;
    font-weight: 400;
    font-size: 19px;
    line-height: 1;
    letter-spacing: 17px;
    padding-left: 17px;
    color: var(--artist-ink);
  }
</style>
</head>
<body>
  <main class="stage">
    <section class="album-cover">
      <div class="cover-artwork" role="img" aria-label="Two figures standing side by side, softly blurred in grey mist above still water"></div>
      <div class="mist-band"></div>
      <svg class="water-surface" viewBox="0 0 720 220" aria-hidden="true">
        <g fill="none" stroke="var(--ripple-line)" stroke-width="1.2">
          <ellipse cx="360" cy="150" rx="70" ry="9"/>
          <ellipse cx="360" cy="150" rx="130" ry="17" stroke-opacity="0.8"/>
          <ellipse cx="360" cy="150" rx="200" ry="26" stroke-opacity="0.6"/>
          <ellipse cx="360" cy="150" rx="280" ry="36" stroke-opacity="0.4"/>
          <ellipse cx="360" cy="150" rx="370" ry="47" stroke-opacity="0.25"/>
        </g>
      </svg>
      <h1 class="album-title">CORVELHA</h1>
      <p class="album-subtitle">(PORTUGUESE FOR DELICATE)</p>
      <p class="artist-name">VELIN SORRE</p>
    </section>
  </main>
</body>
</html>
```